Velmora Flowers Florist Flyer

We are requiring a flyer that advertises and promotes our new business. We specialise in weddings and events but would also like to branch out to corporates and an online subscription. Our brand is feminine/romantic with a touch of elegance and luxury. Our main colour schemes are white, black, gold and pale pink. Instagram: Velmora_flowers and website www.velmoraflowers.com.au
Target Market(s)
brides to be, females
Industry/Entity Type
Florist
Font styles to use
Sans Serif
Script
Other font styles liked:
- The Carpenter
Colors
ffffff
000000
333333
Requirements
Must have
- Feminine/romantic feel, through use of theme colours and elegant font
- our contact details Ph: 0478215096
- email address: contactus@velmoraflowers.com.au
Nice to have
- a description of us willing to work with clients to create their dream wedding flowers. That we offer consultations and no obligation quotes.

```html
<!DOCTYPE html>
<html lang="en">
<head>
<meta charset="utf-8">
<title>Velmora Flowers – Weddings and Events Flyer</title>
<link rel="stylesheet" href="https://fonts.googleapis.com/css2?family=Raleway:wght@300;400&display=swap">
<style>
  :root {
    --stage: #e4e4e4;
    --panel-dark: #2b2728;
    --band-grey: #4b4b4c;
    --gold: #f8c84c;
    --ink: #2b2728;
    --white: #ffffff;
    --photo-green: #3f4f36;
    --photo-blush: #ecd6c8;
    --photo-cream: #f1efe8;
    --photo-red: #7c2a2c;
  }
  * { box-sizing: border-box; margin: 0; padding: 0; }
  html, body {
    width: 1002px; height: 1200px; overflow: hidden;
    background: var(--stage);
    font-family: "Raleway", Arial, sans-serif;
  }
  .flyer {
    position: absolute; left: 37px; top: 0;
    width: 928px; height: 1200px;
    background: var(--panel-dark);
    overflow: hidden;
  }
  .feature-photo {
    position: absolute; left: 0; top: 0; width: 414px; height: 1027px;
    background:
      radial-gradient(ellipse at 45% 60%, var(--photo-blush) 0%, #d9c2b2 30%, transparent 60%),
      linear-gradient(180deg, #4d5b3f 0%, var(--photo-green) 25%, #7d7a66 55%, #b9b2a4 80%, #d8d4cc 100%);
  }
  .info-panel {
    position: absolute; left: 414px; top: 0; width: 514px; height: 1027px;
    background: var(--panel-dark);
  }
  .contact-band {
    position: absolute; left: 0; top: 1027px; width: 928px; height: 173px;
    background: var(--band-grey);
  }
  .detail-photo {
    position: absolute;
    border: 4px solid var(--white);
    border-radius: 18px;
    transform: rotate(45deg);
  }
  .detail-photo--white-roses {
    left: 32px; top: 117px; width: 138px; height: 138px;
    background: linear-gradient(135deg, var(--photo-cream), #c9cfd6 60%, #8f9a8a);
  }
  .detail-photo--red-bouquet {
    left: 216px; top: 28px; width: 192px; height: 192px;
    background: radial-gradient(circle at 50% 50%, var(--photo-red) 0%, #e8e2cf 45%, #4a5a3c 80%);
  }
  .detail-photo--table-roses {
    left: 444px; top: 713px; width: 150px; height: 150px;
    background: linear-gradient(135deg, #b8b3ab, var(--photo-cream) 50%, #7d8a74);
  }
  .detail-photo--posy {
    left: 225px; top: 806px; width: 195px; height: 195px;
    background: radial-gradient(circle at 50% 45%, var(--photo-cream) 0%, #dcdcd4 40%, #5f6e52 80%);
  }
  .headline {
    position: absolute; left: 460px; top: 154px;
    color: var(--gold); font-weight: 300; text-transform: uppercase;
  }
  .headline__line { display: block; font-size: 38px; line-height: 51px; letter-spacing: 0.3px; }
  .headline__line--large { font-size: 98px; line-height: 98px; letter-spacing: 0; margin-left: -4px; }
  .intro {
    position: absolute; left: 460px; top: 458px; width: 400px;
    color: var(--gold); font-size: 15.5px; line-height: 22px; font-weight: 400;
  }
  .intro p + p { margin-top: 18px; }
  .brand-ring {
    position: absolute; left: 484px; top: 742px; width: 396px; height: 396px;
    border-radius: 50%; background: var(--panel-dark);
  }
  .brand-disc {
    position: absolute; left: 523px; top: 781px; width: 318px; height: 318px;
    border-radius: 50%; background: var(--gold);
    display: flex; flex-direction: column; align-items: center; justify-content: center;
    color: var(--ink); font-weight: 400;
  }
  .brand-disc__name { font-size: 50px; line-height: 1; }
  .brand-disc__tag { font-size: 16px; letter-spacing: 8px; margin-top: 8px; text-transform: uppercase; }
  .contact-list {
    position: absolute; left: 74px; top: 1056px; list-style: none;
    color: var(--white); font-size: 19px;
  }
  .contact-list li { display: flex; align-items: center; height: 32px; }
  .contact-list svg { width: 18px; height: 18px; margin-right: 14px; fill: var(--white); }
</style>
</head>
<body>
<main class="flyer">
  <div class="feature-photo" role="img" aria-label="Tall arrangement of blush roses and white snapdragons in a white vase"></div>
  <div class="info-panel"></div>
  <div class="contact-band"></div>

  <div class="detail-photo detail-photo--white-roses" role="img" aria-label="Close view of white and cream roses"></div>
  <div class="detail-photo detail-photo--red-bouquet" role="img" aria-label="Bouquet of red and cream roses with greenery"></div>
  <div class="detail-photo detail-photo--table-roses" role="img" aria-label="White rose table arrangement"></div>
  <div class="detail-photo detail-photo--posy" role="img" aria-label="Small posy of white roses"></div>

  <h1 class="headline">
    <span class="headline__line">Creating stunning</span>
    <span class="headline__line">flowers for</span>
    <span class="headline__line">weddings and</span>
    <span class="headline__line headline__line--large">Events</span>
  </h1>

  <div class="intro">
    <p>With many years of experience behind us and a combined 20 plus years in the industry. We know what we're talking about. We're here to create spectacular floral designs to suit your needs.</p>
    <p>There's nothing more frustrating than having us tell you what to do. At Velmora Flowers you are first and we're here to guide you on your floral journey.</p>
  </div>

  <div class="brand-ring"></div>
  <div class="brand-disc">
    <span class="brand-disc__name">Velmora</span>
    <span class="brand-disc__tag">Flowers</span>
  </div>

  <ul class="contact-list">
    <li>
      <svg viewBox="0 0 24 24" aria-hidden="true"><path d="M6.6 10.8a15.1 15.1 0 0 0 6.6 6.6l2.2-2.2c.3-.3.7-.4 1-.2 1.1.4 2.3.6 3.6.6.6 0 1 .4 1 1V20c0 .6-.4 1-1 1A17 17 0 0 1 3 4c0-.6.4-1 1-1h3.5c.6 0 1 .4 1 1 0 1.3.2 2.5.6 3.6.1.3 0 .7-.2 1z"/></svg>
      0478215096
    </li>
    <li>
      <svg viewBox="0 0 24 24" aria-hidden="true"><path d="M2 5h20v14H2z M4 7v.4l8 5.1 8-5.1V7z" fill-rule="evenodd"/></svg>
      contactus@velmoraflowers.com.au
    </li>
    <li>
      <svg viewBox="0 0 24 24" aria-hidden="true"><rect x="4" y="4" width="16" height="16" rx="2"/></svg>
      Velmora_flowers
    </li>
  </ul>
</main>
</body>
</html>
```